Torlen Caribbean BANK Website Design with UX/UI

I need a website DEV Design Mock up that can be presented in full HTML. Not code needed...just clickable design.
This is a BANk website.
We wil send some websites we like a bit later.
We need at least 10 pages that are Full HTML and integrated.
I will send more Design requirement details.
but feel free to go for it and be ahead

Hi
This is a Bank.
It will be based in the Caribbean. Please read up a bit about the Caribbean so you appreciate our region.
Therefore the only ethnicity that can be used is African American. Go to pixelmarta and search African American People so you can see the ethnicity of the people whom you must feature

The colour Scheme will be those of the Logo. The pantones were provided but it is the BLUE and Yellowish Orange

Target Market(s)

All Bank Customers

Industry/Entity Type

Banking

Number of Pages Required

5+ page

Colors
6b449b
ffc214

Requirements
Must have
• Logo
Follow the Brand Architecture
Use the Pantones provided
Follow the Suite Map Provided
Follow the brief Attached

```html
<!DOCTYPE html>
<html lang="en">
<head>
<meta charset="utf-8">
<title>Torlen Caribbean BANK – Careers</title>
<link href="https://fonts.googleapis.com/css2?family=Open+Sans:wght@400;600&family=Playfair+Display:wght@400&family=Crimson+Text:wght@600;700&display=swap" rel="stylesheet">
<style>
:root{
  --purple:#5a259a;
  --purple-dark:#4b1f86;
  --yellow:#ffc214;
  --ink:#222;
  --muted:#555;
  --line:#cfcfcf;
  --util:#ececec;
  --panel:#f7f7f7;
  --white:#fff;
}
*{margin:0;padding:0;box-sizing:border-box}
html,body{width:773px;height:1200px;overflow:hidden;background:var(--white)}
body{font-family:"Open Sans",sans-serif;color:var(--ink);position:relative}
a{color:inherit;text-decoration:none}
.abs{position:absolute}

/* header */
.util-bar{left:317px;top:0;width:456px;height:24px;background:var(--util);clip-path:polygon(0 0,100% 0,100% 100%,8px 100%)}
.util-links{left:340px;top:7px;font-size:7.3px;color:#333;display:flex;gap:0;white-space:nowrap}
.util-links span{padding:0 7px}
.util-links span:first-child{padding-left:0}
.brand{left:70px;top:32px;display:flex;align-items:center;gap:5px;color:var(--purple);font-weight:600;font-size:15px;line-height:1}
.brand .dot{width:12px;height:12px;border-radius:50%;background:var(--yellow)}
.brand small{display:block;font-size:7px;letter-spacing:2px;margin-top:3px}
.search{left:297px;top:50px;width:299px;height:21px;border:1px solid var(--line);font-size:8px;color:#777;padding:5px 14px}
.search-btn{left:576px;top:50px;width:20px;height:21px;background:var(--yellow)}
.login{left:614px;top:50px;width:90px;height:21px;border:1px solid var(--purple);color:var(--purple);font-size:8.5px;text-align:center;line-height:19px}

.main-nav{left:0;top:92px;width:773px;height:33px;background:var(--purple)}
.main-nav ul{list-style:none;display:flex;position:absolute;left:85px;top:0;height:33px;align-items:center;font-size:8.3px;color:var(--white);white-space:nowrap}
.main-nav li{padding:0 8.5px;border-left:1px solid rgba(255,255,255,.8);line-height:8px}
.main-nav li:first-child{padding-left:0;border:0}
.main-nav li.active{color:var(--yellow);position:relative}
.main-nav li.active::after{content:"";position:absolute;left:8.5px;right:0;bottom:-12px;height:2px;background:var(--yellow)}

/* hero */
.hero{left:0;top:124px;width:773px;height:197px;background:linear-gradient(100deg,#3f5f9a 0%,#6f86b0 40%,#8a6e72 55%,#5c7cad 75%,#7a92bb 100%)}
.hero-kicker{left:68px;top:182px;font-weight:600;font-size:11px;color:var(--yellow);letter-spacing:.3px}
.hero-title{left:66px;top:202px;font-family:"Playfair Display",serif;font-size:23px;color:var(--white)}
.quick{left:669px;width:104px;height:19px;background:var(--white);font-size:7.5px;color:var(--purple);display:flex;align-items:center;padding-left:10px;gap:9px}
.quick svg{width:9px;height:9px}

/* openings */
.section-title{left:68px;top:356px;font-family:"Crimson Text",serif;font-weight:700;font-size:16px;color:var(--purple);letter-spacing:.3px}
.job{left:68px;width:359px;height:101px;border:1px solid var(--line);border-left:3px solid var(--yellow);padding:12px 15px 0 12px}
.job h3{font-weight:400;font-size:10.5px;margin-bottom:3px}
.job p{font-size:8.4px;line-height:14px;color:#333}
.apply{display:inline-block;margin-top:10px;background:var(--purple-dark);color:var(--white);font-size:8.7px;padding:2px 8px;height:17px}

/* right panel */
.side{left:456px;top:345px;width:247px;height:464px;background:var(--panel)}
.side-img{left:473px;top:364px;width:215px;height:214px;background:radial-gradient(circle at 70% 40%,#c98a78 0%,#4d6fa0 30%,#22406c 75%,#1b3356 100%)}
.side h2{left:472px;top:591px;font-weight:400;font-size:13.5px}
.side-copy{left:473px;top:618px;width:230px;font-size:8.4px;line-height:14.65px;color:var(--muted)}
.join{left:467px;top:762px;width:113px;height:24px;background:var(--purple-dark);color:var(--white);font-size:9px;text-align:center;line-height:24px}

/* subscribe */
.subscribe{left:0;top:898px;width:773px;height:57px;background:var(--yellow)}
.subscribe h2{left:67px;top:917px;font-family:"Crimson Text",serif;font-weight:600;font-size:14.5px;color:var(--purple)}
.sub-input{left:321px;top:915px;width:303px;height:25px;background:var(--white);font-size:8.5px;color:#888;padding:7px 15px}
.sub-btn{left:624px;top:915px;width:80px;height:25px;background:var(--purple);color:var(--white);font-size:10px;text-align:center;line-height:25px}

/* footer */
.foot-brand{left:68px;top:980px}
.foot-about{left:68px;top:1054px;width:118px;font-size:8.2px;line-height:12.5px;color:#444}
.foot-col{top:980px}
.foot-col h4{font-family:"Crimson Text",serif;font-weight:700;font-size:11px;color:var(--purple);margin-bottom:5px;white-space:nowrap}
.foot-col ul{list-style:none;font-size:8px;color:#444;line-height:15.3px;white-space:nowrap}
.bottom{left:0;top:1167px;width:773px;height:33px;background:var(--purple)}
.copy{left:68px;top:1179px;font-size:7.8px;color:var(--white)}
.social{top:1174px;width:19px;height:19px;border-radius:50%;background:var(--yellow)}
</style>
</head>
<body>

<header>
  <div class="abs util-bar"></div>
  <nav class="abs util-links"><span>CHECKING</span>|<span>SAVINGS</span>|<span>CREDIT CARDS</span>|<span>LOANS</span>|<span>MORTGAGES</span>|<span>INVESTMENTS</span></nav>
  <a class="abs brand" href="#"><span class="dot"></span><span>Torlen<small>CARIBBEAN</small></span></a>
  <div class="abs search">Search</div>
  <div class="abs search-btn"><svg width="20" height="21" viewBox="0 0 20 21"><circle cx="9.5" cy="9.5" r="3" fill="none" stroke="#fff" stroke-width="1.5"/><line x1="11.6" y1="11.6" x2="13.5" y2="13.5" stroke="#fff" stroke-width="1.6"/></svg></div>
  <a class="abs login" href="#">LOGIN / REGISTER</a>
  <nav class="abs main-nav">
    <ul>
      <li>HOME</li><li>PERSONAL</li><li>SMALL BUSINESS</li><li>PRIVATE BANKING</li><li>CORPORATE</li><li>WEALTH</li><li>ONLINE BANKING</li><li class="active">CAREERS</li>
    </ul>
  </nav>
</header>

<section>
  <div class="abs hero" role="img" aria-label="Two business people shaking hands in front of a city skyline"></div>
  <div class="abs hero-kicker">CAREERS</div>
  <h1 class="abs hero-title">Build Your Future With Us</h1>
  <a class="abs quick" style="top:177px" href="#"><svg viewBox="0 0 10 10"><path d="M3 9V3.5a1 1 0 0 1 2 0V6l3 1v2" fill="none" stroke="#ffc214" stroke-width="1.2"/></svg>APPLY LOANS</a>
  <a class="abs quick" style="top:201px" href="#"><svg viewBox="0 0 10 10"><path d="M1 3.5 5 1l4 2.5zM2 4.5v3.5M4 4.5v3.5M6 4.5v3.5M8 4.5v3.5M1 9h8" fill="none" stroke="#ffc214" stroke-width="1"/></svg>ATM &amp; BRANCH</a>
  <a class="abs quick" style="top:225px" href="#"><svg viewBox="0 0 10 10"><circle cx="5" cy="5" r="4.5" fill="#ffc214"/><text x="5" y="7.4" font-size="7" text-anchor="middle" fill="#fff" font-family="Open Sans,sans-serif" font-weight="600">?</text></svg>HELP &amp; SUPPORT</a>
</section>

<main>
  <h2 class="abs section-title">CURRENT OPENINGS</h2>
  <article class="abs job" style="top:391px"><h3>General Manager (Promoter)</h3><p>Implement sales objective by developing a business plan that covers sale, revenue and expense control. Appoint More..&gt;&gt;</p><a class="apply" href="#">Apply Now</a></article>
  <article class="abs job" style="top:510px"><h3>Branch Sales Manager</h3><p>Implement sales objective by developing a business plan that covers sale, revenue and expense control. Appoint More..&gt;&gt;</p><a class="apply" href="#">Apply Now</a></article>
  <article class="abs job" style="top:629px"><h3>Probatinary Manager</h3><p>Implement sales objective by developing a business plan that covers sale, revenue and expense control. Appoint More..&gt;&gt;</p><a class="apply" href="#">Apply Now</a></article>
  <article class="abs job" style="top:748px"><h3>Assistant Manager</h3><p>Implement sales objective by developing a business plan that covers sale, revenue and expense control. Appoint More..&gt;&gt;</p><a class="apply" href="#">Apply Now</a></article>

  <aside>
    <div class="abs side"></div>
    <div class="abs side-img" role="img" aria-label="Hand touching a digital network of people figures"></div>
    <h2 class="abs" style="left:472px;top:591px;font-weight:400;font-size:13.5px">Great Tomorrows Begin Here!</h2>
    <p class="abs side-copy">A challenging, collaborative and competitive experience brought to you by Careers at email. Opening new spaces and new opportunities! Are you a young, innovative thinker with strategic intent? Do you have the uncanny ability to tease out insights from macro-trends? If yes, then We will shape and fine tune your capabilities. To continue our global success, we are looking for enthusiastic and motivated individuals to be part of our high performing, team oriented culture.</p>
    <a class="abs join" href="#">JOIN WITH US</a>
  </aside>
</main>

<section>
  <div class="abs subscribe"></div>
  <h2 class="abs" style="left:67px;top:917px;font-family:'Crimson Text',serif;font-weight:600;font-size:14.5px;color:var(--purple)">Subscribe here to Get Latest Updates</h2>
  <div class="abs sub-input">Enter your Email Address</div>
  <a class="abs sub-btn" href="#">SUBSCRIBE</a>
</section>

<footer>
  <a class="abs brand foot-brand" href="#"><span class="dot"></span><span>Torlen<small>CARIBBEAN</small></span></a>
  <p class="abs foot-about">To be the premier financial and related services provider to each client we serve world wide, creating wealth..&gt;&gt;</p>
  <div class="abs foot-col" style="left:217px"><h4>Main Links</h4><ul><li>Personal</li><li>Small Business</li><li>Private Banking</li><li>Corporate</li><li>Wealth</li><li>Online Banking</li><li>ATM &amp; Branch</li><li>Careers</li></ul></div>
  <div class="abs foot-col" style="left:321px"><h4>Personal</h4><ul><li>Checking</li><li>Savings</li><li>Credit Cards</li><li>Loans</li><li>Mortgages</li><li>Investments</li><li>Instant Apply</li><li>Rates</li></ul></div>
  <div class="abs foot-col" style="left:413px"><h4>Calculator</h4><ul><li>Mortgage Loan</li><li>Car Loan</li><li>Personal Loan</li><li>Renovation Loan</li><li>Business Loan</li></ul></div>
  <div class="abs foot-col" style="left:520px"><h4>About Us</h4><ul><li>Our Story</li><li>Investor Relations</li><li>Security&nbsp; Center</li><li>Customer Service</li><li>Newsroom</li></ul></div>
  <div class="abs foot-col" style="left:616px"><h4>Customer Support</h4><ul><li>Help&nbsp; &amp; Support</li><li>Contact Us</li><li>Terms and Conditions</li><li>Privacy Policy</li><li>Sitemap</li></ul></div>

  <div class="abs bottom"></div>
  <p class="abs copy">Torlen Caribbean © Copyright 2020.All Rights Reserved.</p>
  <span class="abs social" style="left:610px"></span>
  <span class="abs social" style="left:634px"></span>
  <span class="abs social" style="left:659px"></span>
  <span class="abs social" style="left:684px"></span>
</footer>

</body>
</html>
```